HVAC Company Business Card design with attached logo

Looking for an easily readable and attractive business card design that includes my attached company logo. I selected one sided card because it's more traditional, but I'm open to a 2-sided design. All of the details should be included in the design. Looking to create a professional, upscale image.

Target Market(s)

Commercial and residential consumers

Industry/Entity Type

Hvac

Contact Information for Business Card

Company phone number is 516.738.2945
Company email dennis@pinefieldhvac.example
Company name is Willow Creek Air Conditioning, Refrigeration, and Heating
Dennis Hartwell
Owner Operator
Company Address is
PO Box 782,
527 Tamsworth Rd,
Bethpage, NY 11802
Business License H8179524000
Insured

Font styles to use
Serif
Sans Serif

Colors

Designer to choose colors to be used in the design.

Requirements
Must have
• Must include the logo.
Nice to have
• It seems like it should be a one sided card, but I'm open to a 2 sided one.

```html
<!DOCTYPE html>
<html lang="en">
<head>
<meta charset="utf-8">
<title>Willow Creek – Business Card</title>
<link href="https://fonts.googleapis.com/css2?family=Montserrat:wght@700&family=Roboto:wght@400;500&display=swap" rel="stylesheet">
<style>
  :root {
    --page: #e9eaec;
    --card: #ffffff;
    --blue: #2a4fa3;
    --orange: #f06a1c;
    --ink: #444548;
    --rule: #555658;
  }
  * { box-sizing: border-box; margin: 0; padding: 0; }
  html, body { width: 1200px; height: 1000px; overflow: hidden; }
  body {
    background: var(--page);
    font-family: "Roboto", Arial, sans-serif;
    color: var(--ink);
    position: relative;
  }
  .card {
    position: absolute;
    left: 250px;
    width: 700px;
    height: 400px;
    background: var(--card);
    box-shadow: 0 6px 18px rgba(0,0,0,0.18);
    overflow: hidden;
  }
  .card--front { top: 70px; }
  .card--back  { top: 530px; }

  .brand {
    display: flex;
    align-items: center;
    gap: 14px;
    white-space: nowrap;
  }
  .brand__dot {
    flex: none;
    border-radius: 50%;
    background: var(--orange);
  }
  .brand__name {
    font-family: "Roboto", Arial, sans-serif;
    font-weight: 500;
    color: var(--blue);
    letter-spacing: 0.5px;
    white-space: nowrap;
  }
  .card--front .brand {
    position: absolute;
    left: 50%; top: 50%;
    transform: translate(-50%, -50%);
  }
  .card--front .brand__dot { width: 50px; height: 50px; }
  .card--front .brand__name { font-size: 52px; }

  .card--back .brand { position: absolute; left: 40px; top: 62px; }
  .card--back .brand__dot { width: 32px; height: 32px; }
  .card--back .brand__name { font-size: 30px; }

  .divider {
    position: absolute;
    left: 40px; top: 185px;
    width: 400px; height: 1px;
    background: var(--rule);
  }

  .identity {
    position: absolute;
    right: 30px; top: 36px;
    text-align: right;
  }
  .identity__name {
    font-family: "Montserrat", Arial, sans-serif;
    font-weight: 700;
    font-size: 24px;
    color: var(--blue);
  }
  .identity__role {
    font-size: 15px;
    font-weight: 500;
    color: var(--orange);
    margin-top: 2px;
  }
  .contact {
    list-style: none;
    margin-top: 16px;
    font-size: 14px;
    line-height: 24px;
  }
  .contact li {
    display: flex;
    justify-content: flex-end;
    align-items: center;
    gap: 10px;
    white-space: nowrap;
  }
  .contact__icon { width: 14px; height: 14px; flex: none; }
  .contact .accent { color: var(--blue); }

  .details {
    position: absolute;
    left: 40px; top: 205px;
    font-size: 15px;
    line-height: 21px;
  }
  .details__license-label { color: var(--blue); letter-spacing: 0.5px; margin-right: 4px; }
  .details__license { font-weight: 500; letter-spacing: 0.5px; }
  .details address { font-style: normal; margin-top: 6px; }

  .swoosh { position: absolute; left: 0; top: 0; width: 700px; height: 400px; }
</style>
</head>
<body>

<section class="card card--front" aria-label="Card front">
  <div class="brand">
    <span class="brand__dot"></span>
    <span class="brand__name">Willow Creek</span>
  </div>
</section>

<section class="card card--back" aria-label="Card back">
  <svg class="swoosh" viewBox="0 0 700 400" aria-hidden="true">
    <path d="M0,376 C220,376 420,318 700,246 L700,400 L0,400Z" fill="var(--orange)"/>
    <path d="M0,381 C220,381 420,326 700,257 L700,400 L0,400Z" fill="#fff"/>
    <path d="M0,385 C220,385 420,332 700,264 L700,400 L0,400Z" fill="var(--blue)"/>
    <path d="M0,390 C140,392 300,388 470,400 L0,400Z" fill="#fff"/>
    <path d="M0,393 C130,396 260,396 360,400 L0,400Z" fill="var(--orange)"/>
  </svg>

  <div class="brand">
    <span class="brand__dot"></span>
    <span class="brand__name">Willow Creek</span>
  </div>

  <div class="divider"></div>

  <div class="identity">
    <div class="identity__name">Dennis Hartwell</div>
    <div class="identity__role">Owner Operator</div>
    <ul class="contact">
      <li><span>516.738.2945</span>
        <svg class="contact__icon" viewBox="0 0 16 16" aria-hidden="true"><path d="M3.5 1.5l2.5 3-1.5 1.8c.8 1.8 2.2 3.2 4 4l1.8-1.5 3 2.5-1.3 2.2C7 13.5 2.5 9 1.5 2.8z" fill="var(--blue)"/></svg>
      </li>
      <li><span>dennis@pinefieldhvac.example</span>
        <svg class="contact__icon" viewBox="0 0 16 16" aria-hidden="true"><rect x="1" y="3" width="14" height="10" rx="1" fill="var(--blue)"/><path d="M1.5 3.5L8 9l6.5-5.5" stroke="#fff" stroke-width="1.2" fill="none"/></svg>
      </li>
      <li><span>www.<span class="accent">pinefieldhvac</span>.example</span>
        <svg class="contact__icon" viewBox="0 0 16 16" aria-hidden="true"><circle cx="8" cy="8" r="6.5" fill="none" stroke="var(--blue)" stroke-width="1.4"/><ellipse cx="8" cy="8" rx="2.8" ry="6.5" fill="none" stroke="var(--blue)" stroke-width="1.2"/><path d="M1.5 8h13M2.5 5h11M2.5 11h11" stroke="var(--blue)" stroke-width="1"/></svg>
      </li>
    </ul>
  </div>

  <div class="details">
    <div><span class="details__license-label">License</span><span class="details__license">H8179524000</span></div>
    <address>PO Box 782, 527 Tamsworth Rd,<br>Bethpage, NY 11802</address>
  </div>
</section>

</body>
</html>
```